Business Card Design

Hoping for a black background business card, minimalistic design.
With the Marble Crest logo you created in white.

I would like to include:
My Name and title
Address (street address)
Reception: (phone number)
Fax: (fax number)
Reception: (email address)
Direct email: (email address)
Instagram: (ig handle)

```html
<!DOCTYPE html>
<html lang="en">
<head>
<meta charset="utf-8">
<title>Marble Crest Business Card</title>
<link href="https://fonts.googleapis.com/css2?family=Lato:wght@300;400;700;900&display=swap" rel="stylesheet">
<style>
  :root {
    --backdrop: #3a3a3d;
    --card: #1f1f20;
    --white: #ffffff;
    --silver: #a9a9ab;
    --muted: #5c5c5e;
    --rule: #7d7d80;
    --text-soft: #e8e8e8;
    --icon: #8a8a8c;
  }
  * { margin: 0; padding: 0; box-sizing: border-box; }
  html, body { width: 1200px; height: 913px; overflow: hidden; }
  body {
    background: var(--backdrop);
    font-family: "Lato", sans-serif;
    position: relative;
  }
  .card {
    position: absolute;
    width: 560px;
    height: 320px;
    background: var(--card);
    border-radius: 18px;
    box-shadow: 0 10px 28px rgba(0,0,0,0.45);
    overflow: hidden;
  }
  .card-front { left: 30px; top: 90px; }
  .card-back { left: 610px; top: 503px; }

  /* front */
  .front-mark {
    position: absolute;
    left: 72px; top: 116px;
    width: 88px; height: 88px;
    border: 4px solid var(--silver);
    border-radius: 50%;
  }
  .front-divider {
    position: absolute;
    left: 184px; top: 98px;
    width: 1px; height: 124px;
    background: var(--muted);
  }
  .front-wordmark {
    position: absolute;
    left: 206px; top: 140px;
    font-weight: 300;
    font-size: 30px;
    letter-spacing: 4px;
    line-height: 40px;
    color: var(--muted);
    text-transform: uppercase;
    white-space: nowrap;
  }

  /* back */
  .brand {
    position: absolute;
    right: 36px; top: 40px;
    display: flex;
    align-items: center;
    gap: 12px;
  }
  .brand-circle {
    width: 62px; height: 62px;
    border: 4px solid var(--white);
    border-radius: 50%;
  }
  .brand-name {
    font-weight: 700;
    font-size: 18px;
    letter-spacing: 2px;
    color: var(--white);
    text-transform: uppercase;
    white-space: nowrap;
  }
  .rule-top {
    position: absolute;
    left: 200px; top: 126px;
    width: 330px; height: 1px;
    background: var(--rule);
  }
  .address {
    position: absolute;
    right: 30px; top: 138px;
    text-align: right;
    font-style: normal;
    font-size: 13px;
    line-height: 18px;
    color: var(--text-soft);
  }
  .person-name {
    position: absolute;
    left: 36px; top: 140px;
    font-weight: 900;
    font-size: 28px;
    line-height: 34px;
    letter-spacing: 1px;
    color: var(--muted);
    text-transform: uppercase;
    white-space: nowrap;
  }
  .person-title {
    position: absolute;
    left: 38px; top: 176px;
    font-size: 18px;
    line-height: 22px;
    color: var(--white);
  }
  .rule-bottom {
    position: absolute;
    left: 38px; top: 208px;
    width: 250px; height: 1px;
    background: var(--rule);
  }
  .contacts {
    position: absolute;
    left: 38px; top: 218px;
    list-style: none;
  }
  .contact {
    display: flex;
    align-items: center;
    gap: 10px;
    font-size: 15px;
    line-height: 21px;
    color: var(--white);
    white-space: nowrap;
  }
  .contact svg { width: 14px; height: 14px; flex: none; }
  .contact .fax { margin-left: 4px; }
</style>
</head>
<body>

<section class="card card-front" aria-label="Card front">
  <div class="front-mark"></div>
  <div class="front-divider"></div>
  <div class="front-wordmark">Marble Crest</div>
</section>

<section class="card card-back" aria-label="Card back">
  <div class="brand">
    <span class="brand-name">Marble Crest</span>
    <div class="brand-circle"></div>
  </div>
  <div class="rule-top"></div>
  <address class="address">
    Address, City, State<br>Country, Zip 1235
  </address>

  <h1 class="person-name">Daniel Reyes</h1>
  <p class="person-title">Founder &amp; CEO</p>
  <div class="rule-bottom"></div>

  <ul class="contacts">
    <li class="contact">
      <svg viewBox="0 0 16 16" fill="var(--icon)"><path d="M3 1.5l3 .5 1 3.5-2 1.2a9 9 0 0 0 4.3 4.3l1.2-2 3.5 1 .5 3-2 1.5C7 14 2 9 1.5 3.5z"/></svg>
      <span>(555) 218-4406</span>
      <svg class="fax" viewBox="0 0 16 16" fill="var(--icon)"><rect x="4" y="1" width="8" height="4"/><rect x="1" y="6" width="14" height="6" rx="1"/><rect x="4" y="10" width="8" height="5" fill="var(--card)" stroke="var(--icon)" stroke-width="1.2"/></svg>
      <span>(555) 218-4490</span>
    </li>
    <li class="contact">
      <svg viewBox="0 0 16 16"><rect x="1" y="3" width="14" height="10" fill="var(--icon)"/><path d="M1 3l7 6 7-6" fill="none" stroke="var(--card)" stroke-width="1.3"/></svg>
      <span>desk@frontroomhq.com</span>
    </li>
    <li class="contact">
      <svg viewBox="0 0 16 16"><rect x="1" y="3" width="14" height="10" fill="var(--icon)"/><path d="M1 3l7 6 7-6" fill="none" stroke="var(--card)" stroke-width="1.3"/></svg>
      <span>daniel@northlinemail.com</span>
    </li>
    <li class="contact">
      <svg viewBox="0 0 16 16"><circle cx="8" cy="8" r="6" fill="none" stroke="var(--icon)" stroke-width="1.6"/></svg>
      <span>@marblecrest.studio</span>
    </li>
  </ul>
</section>

</body>
</html>
```